Banner ads for VL that work with same theme as below banners

Love the banner ads below. Need more with attached photos. But use the same wording, font as in below banner ads. Should be VL size 1200/627 so I can use for Trovique and VL. Looking for great ads to use as VL ads. We do lots of ads so it will be worth your time to enter this contest you will be rewarded with a ton of work. Need several banner ads that work together. So maybe 1 of the dresses, 1 of the sweater, 1 of the leggings, 1 of the jacket

Target Market(s)

Women 24-45

Industry/Entity Type

Fashion

Requirements
Must have
• Banner ads that work for VL and Trovique
Nice to have
• Several options to choose from
Should not have
• not sure

```html
<!DOCTYPE html>
<html lang="en">
<head>
<meta charset="utf-8">
<title>Our Best Sweater Ever</title>
<link rel="stylesheet" href="https://fonts.googleapis.com/css2?family=Niconne&family=Old+Standard+TT:wght@400;700&display=swap">
<style>
  :root {
    --band-top: #dcb7c1;
    --band-top-light: #ecd3d6;
    --floor: #f6e5e2;
    --floor-light: #fbf0ee;
    --magenta: #d4146c;
    --script-pink: #c8125f;
    --headline-ink: #343636;
    --button-bg: #1b1a1a;
    --button-text: #f4efe9;
    --photo-grey: #b9b6b8;
    --photo-lilac: #c9c6d6;
    --blossom-white: #f3f1ea;
    --blossom-green: #cfe0bd;
    --rose-pink: #e7a7c3;
    --rose-purple: #c97bb0;
    --flower-pink: #f0bfd0;
    --stem-green: #d9e6c8;
  }
  * { margin: 0; padding: 0; box-sizing: border-box; }
  html, body { width: 1200px; height: 627px; overflow: hidden; background: var(--floor); }
  .banner {
    position: relative;
    width: 1200px;
    height: 627px;
    overflow: hidden;
    background: var(--floor);
  }
  .banner__band {
    position: absolute;
    left: 0; top: 0;
    width: 1200px; height: 318px;
    background: linear-gradient(90deg, var(--band-top) 0%, var(--band-top-light) 55%, var(--band-top) 100%);
  }
  .banner__floor {
    position: absolute;
    left: 0; top: 318px;
    width: 1200px; height: 309px;
    background: radial-gradient(ellipse at 50% 20%, var(--floor-light) 0%, var(--floor) 60%, #f0d7d6 100%);
  }
  .banner__glow {
    position: absolute;
    left: 330px; top: 90px;
    width: 540px; height: 460px;
    background: radial-gradient(ellipse at center, rgba(255,245,242,0.5) 0%, rgba(255,245,242,0) 70%);
  }
  .shapes { position: absolute; left: 0; top: 0; }
  .photo {
    position: absolute;
    border-radius: 60px 60px 0 0;
  }
  .photo--left {
    left: 122px; top: 140px; width: 222px; height: 487px;
    background: linear-gradient(180deg, #c9a27c 0%, var(--photo-grey) 38%, #9d9a9c 100%);
  }
  .photo--right {
    left: 838px; top: 140px; width: 228px; height: 487px;
    background: linear-gradient(180deg, #b98f6c 0%, var(--photo-lilac) 38%, #a7a4b6 100%);
  }
  .florals {
    position: absolute;
    border-radius: 24px;
  }
  .florals--top-left {
    left: 6px; top: 8px; width: 138px; height: 124px;
    background: linear-gradient(135deg, var(--blossom-white) 0%, var(--blossom-white) 55%, var(--blossom-green) 100%);
  }
  .florals--top-right {
    left: 1080px; top: 0; width: 120px; height: 186px;
    border-radius: 0 0 0 28px;
    background: linear-gradient(160deg, var(--rose-purple) 0%, var(--rose-pink) 55%, #d6c9b6 100%);
  }
  .florals--bottom-left {
    left: 0; top: 362px; width: 150px; height: 265px;
    border-radius: 0 28px 0 0;
    background: linear-gradient(180deg, var(--stem-green) 0%, var(--flower-pink) 45%, var(--stem-green) 100%);
  }
  .headline {
    position: absolute;
    left: 350px; top: 0;
    width: 500px; height: 400px;
    text-align: center;
    font-weight: normal;
  }
  .headline__script {
    position: absolute;
    left: 0; width: 500px;
    font-family: "Niconne", cursive;
    font-weight: 400;
    font-size: 72px;
    line-height: 1;
    color: var(--script-pink);
    letter-spacing: 9px;
  }
  .headline__script--top { top: 146px; padding-left: 20px; }
  .headline__script--bottom { top: 322px; padding-left: 6px; }
  .headline__main {
    position: absolute;
    left: 0; top: 222px; width: 500px;
    font-family: "Old Standard TT", serif;
    font-weight: 700;
    font-size: 70px;
    line-height: 1;
    letter-spacing: 7px;
    color: var(--headline-ink);
  }
  .cta {
    position: absolute;
    left: 487px; top: 421px;
    width: 226px; height: 57px;
    background: var(--button-bg);
    color: var(--button-text);
    font-family: "Old Standard TT", serif;
    font-size: 15px;
    letter-spacing: 2.5px;
    display: flex;
    align-items: center;
    justify-content: center;
    text-decoration: none;
  }
  .cta__strong { font-weight: 700; }
  .cta__light { font-weight: 400; margin: 0 6px; }
</style>
</head>
<body>
  <div class="banner">
    <div class="banner__band"></div>
    <div class="banner__floor"></div>
    <div class="banner__glow"></div>

    <svg class="shapes" width="1200" height="627" viewBox="0 0 1200 627" aria-hidden="true">
      <polygon points="0,0 82,0 0,188" fill="var(--magenta)"/>
      <polygon points="0,312 108,312 100,320 0,320" fill="var(--magenta)"/>
      <polygon points="1102,312 1200,312 1200,320 1094,320" fill="var(--magenta)"/>
    </svg>

    <div class="florals florals--top-left" role="img" aria-label="White blossom branch with green leaves"></div>
    <div class="florals florals--top-right" role="img" aria-label="Bouquet of pink and purple roses"></div>
    <div class="florals florals--bottom-left" role="img" aria-label="Pink flowers with green swirling stems"></div>

    <div class="photo photo--left" role="img" aria-label="Model wearing an oversized grey knit turtleneck sweater"></div>
    <div class="photo photo--right" role="img" aria-label="Model wearing an oversized lilac knit turtleneck sweater"></div>

    <h1 class="headline">
      <span class="headline__script headline__script--top">Our Best</span>
      <span class="headline__main">SWEATER</span>
      <span class="headline__script headline__script--bottom">Ever!</span>
    </h1>

    <a class="cta" href="#">
      <span class="cta__strong">SHOP</span><span class="cta__light">THE</span><span class="cta__strong">LOOK</span>
    </a>
  </div>
</body>
</html>
```